Tolvik's Trim spring flyers

I am needing a flyer design for my lawn mowing business. my services are mowing, edging, weed eating, vacuuming with strong attention to detail. residential and commercial. Mowing average $35 and Spring clean up average $79. Looking for fun, professional and colorful to grab the eye and stand out. rough sizing of 10"x4"

Target Market(s)

people needing lawn care and spring clean up

Font styles to use
Serif

Colors

Designer to choose colors to be used in the design.

Requirements
Must have
• Services listed and pricing listed
• please add licensed and insured
• 417-555-0183
• dorsebrian7@fernmail.test
• FREE ESTIMATES

```html
<!DOCTYPE html>
<html lang="en">
<head>
<meta charset="utf-8">
<title>Tolvik's Trim spring flyers</title>
<link href="https://fonts.googleapis.com/css2?family=Kumbh+Sans:wght@500;600;700;800&display=swap" rel="stylesheet">
<style>
  :root {
    --brand-blue: #1a6db5;
    --sky-top: #2f86d0;
    --sky-mid: #5fb0e8;
    --cloud: #e9f3fb;
    --lawn: #5bb33a;
    --lawn-deep: #3d8c2a;
    --price-green: #6ab531;
    --ink: #2c2d3a;
    --seal: #1e2238;
    --seal-rim: #c9ccd6;
    --paper: #ffffff;
  }
  * { margin: 0; padding: 0; box-sizing: border-box; }
  html, body {
    width: 1111px; height: 1200px; overflow: hidden;
    background: var(--paper);
    font-family: "Kumbh Sans", sans-serif;
  }
  .flyer {
    position: absolute; top: 34px; width: 454px; height: 1135px;
    background: var(--paper);
    box-shadow: 0 0 4px rgba(0,0,0,.18);
    overflow: hidden;
  }
  .flyer--services { left: 74px; }
  .flyer--pricing { left: 581px; }

  .brand-name {
    position: absolute; left: 0; right: 0; text-align: center;
    color: var(--brand-blue); font-weight: 700; letter-spacing: -0.5px;
  }
  .flyer--services .brand-name { top: 160px; font-size: 48px; }
  .flyer--pricing .brand-name { top: 108px; font-size: 32px; }
  .brand-mark {
    position: absolute; left: 50%; transform: translateX(-50%);
    border-radius: 50%; background: var(--brand-blue);
  }
  .flyer--services .brand-mark { top: 70px; width: 70px; height: 70px; }
  .flyer--pricing .brand-mark { top: 48px; width: 48px; height: 48px; }

  .scene { position: absolute; left: 0; right: 0; }
  .scene--home {
    top: 269px; height: 790px;
    background: linear-gradient(180deg, var(--cloud) 0%, var(--sky-top) 14%, var(--sky-mid) 55%, var(--lawn) 78%, var(--lawn-deep) 90%, #eef3ea 100%);
  }
  .scene--garden {
    top: 198px; height: 672px;
    background: linear-gradient(180deg, var(--cloud) 0%, var(--sky-top) 16%, #9bc6df 36%, var(--lawn-deep) 55%, var(--lawn) 78%, #f4f8f1 100%);
  }

  .service-list {
    position: absolute; top: 458px; left: 0; right: 0;
    text-align: center; color: var(--paper);
    font-size: 56px; font-weight: 600; line-height: 66px;
    list-style: none;
  }

  .price-tag { position: absolute; width: 188px; height: 164px; }
  .price-tag svg { position: absolute; inset: 0; }
  .price-tag p {
    position: relative; height: 100%;
    display: flex; flex-direction: column; justify-content: center; align-items: center;
    color: var(--price-green); font-weight: 700; font-size: 34px; line-height: 40px; text-align: center;
  }
  .price-tag--mowing { left: 57px; top: 234px; }
  .price-tag--cleanup { left: 212px; top: 446px; }
  .price-tag--cleanup p { font-size: 32px; line-height: 38px; }

  .seal {
    position: absolute; left: 214px; top: 766px; width: 160px; height: 160px;
    border-radius: 50%;
    background: radial-gradient(circle at 40% 35%, #3a3f5c 0%, var(--seal) 65%);
    border: 6px solid var(--seal-rim);
    display: flex; align-items: center; justify-content: center;
  }
  .seal__text {
    transform: rotate(-18deg);
    color: var(--paper); font-weight: 800; font-size: 22px; line-height: 26px;
    text-align: center; text-transform: uppercase; letter-spacing: 0.3px;
  }

  .contact {
    position: absolute; left: 0; right: 0; text-align: center; color: var(--ink); font-weight: 600;
  }
  .contact--phone { top: 954px; font-size: 31px; }
  .contact--email { top: 994px; font-size: 26px; font-weight: 500; }

  .estimate-button {
    position: absolute; left: 24px; width: 408px; top: 1056px; height: 90px;
    background: var(--price-green);
    border-radius: 60px 60px 0 0;
    color: var(--paper); font-size: 38px; font-weight: 700;
    display: flex; align-items: flex-start; justify-content: center; padding-top: 20px;
  }
</style>
</head>
<body>
  <section class="flyer flyer--services">
    <div class="brand-mark"></div>
    <h1 class="brand-name">Tolvik's Trim</h1>
    <div class="scene scene--home" role="img" aria-label="Photo of a large suburban house with a neat green lawn, flowering shrubs and blue sky with clouds"></div>
    <ul class="service-list">
      <li>Lawn mowing,</li>
      <li>edging,</li>
      <li>weed eating,</li>
      <li>vacuuming</li>
    </ul>
  </section>

  <section class="flyer flyer--pricing">
    <div class="brand-mark"></div>
    <h2 class="brand-name">Tolvik's Trim</h2>
    <div class="scene scene--garden" role="img" aria-label="Photo of a garden with a wooden gazebo, trimmed round shrubs and a gloved hand using hedge shears on the lawn"></div>
    <div class="price-tag price-tag--mowing">
      <svg viewBox="0 0 188 164" aria-hidden="true"><polygon points="0,82 47,0 141,0 188,82 141,164 47,164" fill="#fff"/></svg>
      <p><span>Mowing</span><span>$35</span></p>
    </div>
    <div class="price-tag price-tag--cleanup">
      <svg viewBox="0 0 188 164" aria-hidden="true"><polygon points="0,82 47,0 141,0 188,82 141,164 47,164" fill="#fff"/></svg>
      <p><span>Spring</span><span>clean up</span><span>$79</span></p>
    </div>
    <div class="seal">
      <p class="seal__text">Licensed<br>&amp; Insured</p>
    </div>
    <p class="contact contact--phone">417-555-0183</p>
    <p class="contact contact--email">dorsebrian7@fernmail.test</p>
    <div class="estimate-button">FREE ESTIMATES</div>
  </section>
</body>
</html>
```